1. 商品のコンセプト:鉢植えの植物を元気にみずみずしく保つ。お客様に代わって心を込めたお手入れを。
2. 商品コンセプトの理由:水やり以外のお手入れは放置しがちな鉢植えも、お手入れすることで美しく保てることで、安らぎや楽しみを与えてくれる存在となります。
3. 販売価格:(価格はすべて税込み)
【植替え】
新しく植え替える鉢の上部直径
15㎝(5号鉢)まで 3,500円
21㎝(7号鉢)まで 6,000円
30㎝(10号鉢)まで 9,000円
45㎝(15号鉢)まで 15,000円
※ただし、盆栽は除く
●料金は作業代のみの価格となります。
●植替えで必要な鉢や土などは、お客さまがご用意いただければ別途費用がかからず、そちらを使用して作業致します。
ただし、樹種や状態によって必要な鉢のサイズや土の種類や量がありますので、お見積り時にご相談のうえご用意いただけるのが望ましいです。
●また、鉢や土など当社でご用意することも可能です。その場合、別途お見積りとなります。
●古い土は、ご希望があればお引き取りいたします(別途見積り)
●不要になった鉢のお引き取りは、ご相談ください(別途見積り)
※ただし、プラスチック、金属、ガラス、樹脂、コンクリートなどはお引き取りできません。
【剪定】形を整えたり、高さを調整したりします。
高さ3m未満 4,000円/本
【消毒】病害虫の症状にあわせた薬剤は散布し予防や駆除をします。
高さ3m未満 2,000円/本
【施肥】肥料を施して栄養分を補い、成育促進、花付き、実付きの改善をします。
3,000円より
4. 販売方法
お見積り無料
ご依頼(電話・WEB)→担当から連絡→無料見積り(お客様宅へ出向いて実際のものを見てお見積りをします。見積書有効期限1か月)→ご依頼(作業日時決定)→作業→お支払い(郵便局・銀行から振り込み、コンビニエンスストアでのお支払い(コンビニ後払い)、クレジットカード決済)

[強み]
1鉢からでも承ります。お見積り無料。お客さまご自身で植替えに必要な鉢や土などを担当者にご相談のうえご用意いただけたら、費用は作業代のみとなります(土やゴミの回収ご希望の場合は別途費用がかかります)
社名、ロゴ、電話番号、URL、QRコード
A4
両面
緑系、水色系、茶系、こだわりはそれ程強くないので、色合いはお任せします。
• イラストレーター形式 (.ai)
弊社HP
https://www.375m.co.jp/
各種メニューと価格
https://www.375m.co.jp/price/

鉢植えの植替えや鉢植えのお手入れに関する素材については、フリー素材等にて適宜入れてください。
必要に応じてリクエストさせていただきたいと思います。

必要な情報が一通り網羅されていました。
シンプルに当社のサービスを表現されていました。

短期間の中多くのご提案をいただき、誠にありがとうございました。
どのご提案もレベルが高く、良い意味で選定に苦慮しました。
また新たなチラシ作成の際は是非ご提案いただければ幸いです。

```html
<!DOCTYPE html>
<html lang="ja">
<head>
<meta charset="utf-8">
<title>みどり手帖 鉢植えのお手入れ</title>
<link rel="stylesheet" href="https://fonts.googleapis.com/css2?family=Noto+Sans+JP:wght@400;500;700;900&display=swap">
<style>
  :root {
    --green: #3f9c3a;
    --green-deep: #2f7f2c;
    --ink: #333333;
    --ink-soft: #555555;
    --paper: #ffffff;
    --rule: #d9d9d9;
  }
  * { margin: 0; padding: 0; box-sizing: border-box; }
  html, body { width: 851px; height: 1200px; overflow: hidden; background: var(--paper); }
  body { font-family: "Noto Sans JP", sans-serif; color: var(--ink); }
  .flyer { position: relative; width: 851px; height: 1200px; background: var(--paper); }
  .hero-photo {
    position: absolute; left: 0; top: 0; width: 851px; height: 690px;
    background:
      radial-gradient(ellipse at 20% 25%, #4f7d3a 0%, transparent 45%),
      radial-gradient(ellipse at 85% 20%, #5e8f42 0%, transparent 40%),
      radial-gradient(ellipse at 55% 10%, #e8efe2 0%, transparent 35%),
      linear-gradient(180deg, #cfdcc4 0%, #8fae74 45%, #6f9a4e 70%, #7fa85a 100%);
  }
  .brand-panel {
    position: absolute; left: 48px; top: 522px; width: 732px; height: 268px;
    background: var(--paper); padding: 26px 0 0 14px;
  }
  .brand-roman {
    display: flex; align-items: center; gap: 12px;
    font-size: 30px; font-weight: 700; letter-spacing: 1px; color: var(--green);
  }
  .brand-roman .dot { width: 20px; height: 20px; border-radius: 50%; background: var(--green); }
  .brand-name {
    margin-top: 4px; font-size: 112px; font-weight: 700; line-height: 1.08;
    color: var(--green); letter-spacing: 2px;
  }
  .tagline {
    margin-top: 14px; font-size: 33px; font-weight: 700; color: var(--ink-soft); letter-spacing: 1px;
  }
  .concept { position: absolute; left: 0; top: 838px; width: 851px; text-align: center; }
  .concept .rule { width: 690px; height: 1px; background: var(--rule); margin: 0 auto 14px; }
  .concept p { font-size: 14.5px; line-height: 1.75; color: var(--ink); }
  .concept p + p { margin-top: 28px; }
  .company {
    position: absolute; left: 0; top: 1140px; width: 851px; text-align: center;
    font-size: 14px; color: var(--ink);
  }
</style>
</head>
<body>
  <main class="flyer">
    <div class="hero-photo" role="img" aria-label="木立に囲まれた緑の芝生にテントが並ぶ明るいキャンプ場の写真"></div>

    <section class="brand-panel">
      <div class="brand-roman"><span>MIDORI</span><span class="dot"></span><span>TECHO</span></div>
      <h1 class="brand-name">みどり手帖</h1>
      <p class="tagline">私たちは日本のお庭を笑顔にします</p>
    </section>

    <section class="concept">
      <div class="rule"></div>
      <p>鉢植えの植物を元気にみずみずしく保つ。お客様に代わって心を込めたお手入れを。</p>
      <p>水やり以外のお手入れは放置しがちな鉢植えも、お手入れすることで美しく保てることで、<br>安らぎや楽しみを与えてくれる存在となります。</p>
    </section>

    <p class="company">株式会社ミナモ・ガーデン</p>
  </main>
</body>
</html>
```